Games in Classrooms Sponsorship Brochure

We need a 4 page sponsorship booklet designed for Games in Classrooms. Games in Classrooms is a scheme that brings top GB athletes into primary schools to encourage children to lead a healthy life and raise much needed funds for schools to buy new sports equipment. We would like to see designs that are eye catching, colourful and would appeal to children. I have attached the Kids at Heart Appeal Kit (FULL PACK) for design ideas and a Word Document containing potential content (Sponsorship Form - Generic.docx) . I have also attached our brand guidelines and colour palette (Brand Guidelines PPT). WE would like to see pictures of our events and athletes to help bring the sponsorship form to life. I have attached some examples but please feel free to ask for more.

Target Market(s)

Children/Parents and Families/Friends

Requirements
Must have
• 4 pages
• Be a booklet
• Have a sponsorship form on the front
• Be eye catching
• Be colourful

```html
<!DOCTYPE html>
<html lang="en">
<head>
<meta charset="utf-8">
<title>Games in Classrooms – Get Your Friends and Family Involved</title>
<link href="https://fonts.googleapis.com/css2?family=Open+Sans:wght@400;600;700&display=swap" rel="stylesheet">
<style>
  :root{
    --backdrop:#65646f;
    --paper:#ffffff;
    --ink:#1d1d1b;
    --red:#e30613;
    --green:#4aa92f;
    --blue:#3a87cb;
    --sky:#3fb2e6;
    --navy:#4f72b8;
    --photo-a:#c9a46e;
    --photo-b:#7a6a5a;
  }
  *{box-sizing:border-box;margin:0;padding:0}
  html,body{width:1200px;height:1200px;overflow:hidden;background:var(--backdrop)}
  body{font-family:"Open Sans",Arial,sans-serif;color:var(--ink)}
  .page{position:absolute;left:176px;top:0;width:848px;height:1200px;background:var(--paper)}
  .abs{position:absolute}
  .headline{left:219px;top:32px;font-size:35px;font-weight:700;color:var(--blue);letter-spacing:.3px;white-space:nowrap}
  .dot{position:absolute;border-radius:50%}
  .dot.red{background:var(--red)} .dot.green{background:var(--green)} .dot.blue{background:var(--blue)}
  .copy{font-size:16px;line-height:20.5px;white-space:nowrap}
  .copy b{font-weight:700}
  .event-icon{left:218px;top:90px;width:76px;height:76px;border-radius:50%;background:var(--red);display:flex;align-items:center;justify-content:center}
  .photo{left:293px;top:173px;width:613px;height:411px;border:4px solid var(--green);border-radius:3px;padding:2px;background:var(--paper)}
  .photo div{width:100%;height:100%;background:linear-gradient(160deg,var(--photo-b) 0%,var(--photo-a) 55%,#d8b47a 100%)}
  .step-num{font-size:66px;line-height:1;font-weight:400;left:214px}
  .step-num span{font-size:40px}
  .step-box{left:280px;width:102px;height:77px;display:flex;align-items:center;justify-content:center}
  .step-title{font-size:18px;font-weight:700;line-height:22px}
  .step-text{font-size:16px;line-height:20.5px;white-space:nowrap}
  .sq{left:218px;width:53px;height:52px;border-radius:8px;display:flex;align-items:center;justify-content:center}
  .callout{left:709px;top:859px;width:224px;height:178px;border:4px solid var(--blue);border-radius:50%;display:flex;align-items:center;justify-content:center;text-align:center;font-size:16.5px;line-height:20.5px}
</style>
</head>
<body>
<main class="page" aria-label="Get your friends and family involved"></main>

<h1 class="abs headline">GET YOUR FRIENDS AND FAMILY INVOLVED</h1>

<div class="abs event-icon">
  <svg width="42" height="32" viewBox="0 0 42 32"><rect x="7" y="3" width="28" height="20" rx="2" fill="none" stroke="#fff" stroke-width="3"/><path d="M2 26h38l-3 4H5z" fill="#fff"/></svg>
</div>
<p class="abs copy" style="left:306px;top:104px">Find out more about your event and the Athlete visiting your schools at<br><b>www.GamesInClassrooms.org/MyEvent</b></p>

<div class="abs photo"><div role="img" aria-label="Photo of an athlete crawling on all fours alongside primary school children during a sports hall session"></div></div>

<!-- decorative dots -->
<span class="dot blue" style="left:943px;top:94px;width:34px;height:34px"></span>
<span class="dot green" style="left:672px;top:129px;width:26px;height:26px"></span>
<span class="dot green" style="left:212px;top:232px;width:50px;height:50px"></span>
<span class="dot red" style="left:237px;top:324px;width:12px;height:12px"></span>
<span class="dot blue" style="left:215px;top:391px;width:44px;height:44px"></span>
<span class="dot green" style="left:954px;top:282px;width:38px;height:38px"></span>
<span class="dot red" style="left:913px;top:379px;width:52px;height:52px"></span>
<span class="dot green" style="left:855px;top:612px;width:36px;height:36px"></span>
<span class="dot blue" style="left:919px;top:636px;width:72px;height:72px"></span>
<span class="dot red" style="left:648px;top:687px;width:28px;height:28px"></span>
<span class="dot red" style="left:933px;top:875px;width:32px;height:32px"></span>
<span class="dot green" style="left:626px;top:1008px;width:16px;height:16px"></span>
<span class="dot red" style="left:904px;top:1071px;width:84px;height:84px"></span>

<!-- step 1 -->
<div class="abs step-num" style="top:612px;color:var(--red)">1<span>.</span></div>
<div class="abs step-box" style="top:607px;background:var(--red)">
  <svg width="58" height="44" viewBox="0 0 58 44"><rect x="2" y="2" width="54" height="40" rx="3" fill="none" stroke="#fff" stroke-width="3"/><line x1="2" y1="10" x2="56" y2="10" stroke="#fff" stroke-width="2"/><path d="M29 16l9 4v10l-9 4-9-4V20z" fill="none" stroke="#fff" stroke-width="2.5"/><path d="M20 20l9 4 9-4M29 24v10" fill="none" stroke="#fff" stroke-width="2"/></svg>
</div>
<div class="abs" style="left:395px;top:616px">
  <p class="step-title" style="color:var(--red)">Set up an online fundraising page</p>
  <p class="step-text">(takes 90 seconds) Simply visit<br><b>www.gamesinclassrooms.org/sponsormychild</b></p>
</div>

<!-- step 2 -->
<div class="abs step-num" style="top:701px;color:var(--green)">2<span>.</span></div>
<div class="abs step-box" style="top:698px;background:var(--green)">
  <svg width="40" height="48" viewBox="0 0 40 48"><rect x="6" y="26" width="28" height="20" fill="#fff"/><circle cx="20" cy="16" r="6" fill="none" stroke="#fff" stroke-width="2.5"/><path d="M6 8q10-8 28-2" fill="none" stroke="#fff" stroke-width="3"/><line x1="20" y1="22" x2="20" y2="28" stroke="var(--green)" stroke-width="3"/></svg>
</div>
<div class="abs" style="left:395px;top:705px">
  <p class="step-title" style="color:var(--green)">Make the 1st donation</p>
  <p class="step-text">The best way to encourage others to support your child is to be<br>the first to sponsor them. The amount is less important than the act!</p>
</div>

<!-- step 3 -->
<div class="abs step-num" style="top:791px;color:var(--blue)">3<span>.</span></div>
<div class="abs step-box" style="top:787px;background:var(--blue)">
  <svg width="50" height="42" viewBox="0 0 50 42"><circle cx="32" cy="11" r="8" fill="none" stroke="#fff" stroke-width="3"/><path d="M22 36q2-14 10-14t12 14z" fill="none" stroke="#fff" stroke-width="3"/><circle cx="18" cy="15" r="8" fill="#fff"/><path d="M4 40q2-15 14-15t14 15z" fill="#fff"/></svg>
</div>
<div class="abs" style="left:397px;top:793px">
  <p class="step-title" style="color:var(--blue)">Invite others</p>
  <p class="step-text">Share your child’s fundraising page with friends and family to get the<br>donations rolling in.</p>
</div>

<!-- social -->
<div class="abs sq" style="top:896px;background:var(--sky)"></div>
<p class="abs copy" style="left:282px;top:911px">See tweets and pictures from our events <b>@gamesinclass</b></p>

<div class="abs sq" style="top:964px;background:var(--navy)"></div>
<p class="abs copy" style="left:280px;top:980px">See our fun facts on Faceboard <b>@gamesinclassrooms</b></p>

<div class="abs callout"><p>We’d love to hear<br>from you – post us<br>your pictures and<br>comments on<br>social media</p></div>

<div class="abs sq" style="top:1034px;background:var(--red)">
  <svg width="36" height="36" viewBox="0 0 36 36"><rect x="2" y="4" width="32" height="10" rx="2" fill="none" stroke="#fff" stroke-width="2"/><path d="M18 33V19m-7 6l7-7 7 7" fill="none" stroke="#fff" stroke-width="2.5"/></svg>
</div>
<p class="abs copy" style="left:281px;top:1041px">Sign up to our bite size articles about health, nutrition and exercise at<br><b>www.gamesinclassrooms.org</b></p>

<div class="abs sq" style="top:1102px;background:var(--green)">
  <svg width="14" height="34" viewBox="0 0 14 34"><circle cx="7" cy="5" r="4" fill="#fff"/><rect x="2.5" y="12" width="9" height="21" fill="#fff"/></svg>
</div>
<p class="abs copy" style="left:281px;top:1110px">To find out more about Games in Classrooms and how we fund the scheme,<br>visit:&nbsp;&nbsp; <b>www.GamesInClassrooms.org/funding-for-schools/</b></p>
</body>
</html>
```